Wordpress Contest Brief I would like a WordPress theme designed

Industry / Entity Type

Financial consultancy / advisers

Current site is: http://www.quorvel-group.com

Looking for a complete overhaul of this site, we are after a clean modern look. Will require the ability to easily add, update and remove content, hence the WordPress design.
Example:
Add case studies
Industry documentation (downloadable brochures / flyers and such)

What we like from our current site is the colour the fonts and the logo (the city of London) we would like to have other city outlines (NYC and Tokyo, Hong Kong, Singapore).

The site will be used by our potential clients to get in contact and re-view the case studies, if possible would like to have a client login area where they can download our documents like NDA’s etc and T&C’s.

Task Outline

Create a Web Design (Coded - Design and coding required)
Designer must provide full implementation/coding depending on the platform chosen by the client (i.e. WordPress theme, HTML/CSS, bootstrap etc.)

Task Description

I need a full website built that must work on desktop and mobile. I can provide the London city skyline and the font file, which we have used. Some stock industrial photos will be required.

Requirements:

*Splash page
*What We Do
*How We do it
*Who Are We? To have the same information and links as the current site
*Why use us?
*Clients: To have the same information and links as the current site
*Partners: To have the same information and links as the current site
*Contact:

Target Market(s)

Financial institutions trading Equities, Futures, Options, Forex and Fixed Income.
Regulators, Exchanges, ECN’s
Buy side firms and Sell side firms

Industry/Entity Type

Financial

Coding

Coded - Design and coding required

Number of Pages Required

5+ page

Font styles to use
Sans Serif

Colors
f04a50

Requirements
Must have
• Splash page
• What We Do
• How We do it
• Who Are We? To have the same information and links as the current site
• Why use us?
• Clients: To have the same information and links as the current site
• Partners: To have the same information and links as the current site
• Contact:

```html
<!DOCTYPE html>
<html lang="en">
<head>
<meta charset="utf-8">
<title>Quorvel Group — Advisory</title>
<link href="https://fonts.googleapis.com/css2?family=Michroma&family=Raleway:ital,wght@0,400;0,500;0,600;0,700;0,800;1,400&display=swap" rel="stylesheet">
<style>
:root{
  --red:#f04a50;
  --red-soft:#ef6b6e;
  --dark:#2b2627;
  --darker:#231f20;
  --hero:#4a4748;
  --ink:#333;
  --muted:#777;
  --line:#d6d6d6;
  --white:#fff;
}
*{margin:0;padding:0;box-sizing:border-box}
html,body{width:1200px;height:3896px;overflow:hidden}
body{position:relative;background:var(--white);font-family:'Raleway',sans-serif;color:var(--ink)}
.abs{position:absolute}
.display{font-family:'Michroma',sans-serif;font-weight:400}

/* Top bar + header */
.topbar{left:0;top:0;width:1200px;height:40px;font-size:11px;color:#ddd;z-index:3}
.topbar .item{position:absolute;top:13px;display:flex;align-items:center;gap:8px}
.topbar svg{width:14px;height:14px}
.masthead{left:0;top:40px;width:1200px;height:48px;border-bottom:1px solid rgba(255,255,255,.15);z-index:3}
.brand{position:absolute;left:70px;top:8px;font-size:15px;letter-spacing:3px;color:#eee;text-transform:uppercase;font-weight:500}
.nav{position:absolute;left:683px;top:8px;display:flex;gap:26px;font-size:11px;font-weight:700;color:#eee}
.nav a{color:inherit;text-decoration:none;padding-bottom:10px}
.nav a.active{border-bottom:2px solid var(--white)}

/* Hero */
.hero{left:0;top:0;width:1200px;height:550px;background:linear-gradient(180deg,#5a5758 0%,#4a4748 55%,#3f3c3d 100%)}
.hero-skyline{left:0;top:240px;width:1200px;height:310px;background:linear-gradient(180deg,rgba(40,37,38,0) 0%,rgba(40,37,38,.75) 45%,#2f2c2d 100%)}
.hero-kicker{left:267px;top:158px;background:#1d1b1c;color:var(--white);font-weight:800;font-size:27px;letter-spacing:1px;padding:2px 14px;text-transform:uppercase}
.hero-title{left:282px;top:205px;color:var(--white);font-weight:800;font-size:40px;line-height:44px;text-transform:uppercase}

/* Who we are */
.h2{font-size:28px;letter-spacing:4px;color:#222}
.who-title{left:234px;top:622px}
.who-quote{left:234px;top:692px;width:390px;font-size:9px;font-style:italic;color:#444}
.who-body{left:234px;top:725px;width:390px;font-size:10.5px;line-height:14px;color:#666}
.who-body p+p{margin-top:10px}
.who-sign{left:234px;top:980px;font-size:13px;letter-spacing:4px;color:#333;text-transform:uppercase}
.who-panel{left:675px;top:623px;width:281px;height:390px;background:linear-gradient(160deg,var(--red-soft),var(--red))}
.who-panel p{position:absolute;left:34px;top:90px;width:220px;color:var(--white);font-size:14px;line-height:26px;letter-spacing:3px;text-transform:uppercase;font-weight:500}

/* What we do */
.what-title{left:0;top:1160px;width:1200px;text-align:center}
.what-intro{left:244px;top:1240px;font-size:10.5px;color:#666}
.service{position:absolute;top:1291px;width:222px}
.service .photo{height:163px}
.service h3{display:flex;align-items:center;gap:12px;margin-top:24px;font-size:14px;font-weight:700;color:#222}
.dot{width:34px;height:34px;border-radius:50%;background:var(--red);flex:none}
.service p{margin-top:14px;font-size:10.5px;line-height:14px;color:#777}

/* CTA */
.cta{left:0;top:1714px;width:1200px;height:156px;background:var(--dark)}
.cta h2{position:absolute;left:117px;top:32px;font-size:20px;letter-spacing:3px;color:var(--white)}
.cta p{position:absolute;left:117px;top:72px;font-size:15px;color:#ddd}
.cta-btn{position:absolute;left:865px;top:34px;width:174px;height:54px;background:var(--red);color:var(--white);font-size:16px;display:flex;align-items:center;justify-content:center;letter-spacing:.5px}

/* Why choose */
.why-photo{left:156px;top:1872px;width:402px;height:621px;background:linear-gradient(180deg,#eef1f4 0%,#c9d6e6 40%,#8ea7c9 75%,#3c4f6e 100%)}
.why-title{left:587px;top:1930px}
.why-body{left:587px;top:2000px;width:470px;font-size:13.5px;line-height:18px;color:#555}
.feature{position:absolute;width:210px}
.feature h4{display:flex;align-items:center;gap:12px;font-size:14px;font-weight:700;color:#222}
.feature p{margin-top:10px;font-size:10.5px;line-height:14px;color:#777}

/* Team */
.team{left:0;top:2493px;width:1200px;height:753px;background:linear-gradient(180deg,#e86669 0%,#d9575b 100%)}
.team-title{left:0;top:105px;width:1200px;text-align:center;color:var(--white)}
.team-lead{left:234px;top:175px;color:var(--white);font-size:14px}
.team-body{left:234px;top:210px;width:770px;color:var(--white);font-size:14px;line-height:19px}
.member{position:absolute;top:364px;width:266px}
.member .frame{height:218px;background:var(--white);padding:26px 50px}
.member .portrait{height:166px;background:linear-gradient(180deg,#c7cfd6 0%,#8f9eab 60%,#4f6275 100%)}
.member ul{list-style:none;margin-top:22px;padding-left:58px;color:var(--white);font-size:10px;line-height:22px}

/* Contact */
.contact-title{left:125px;top:3330px;font-size:17px;letter-spacing:3px;color:#222}
.contact-body{left:125px;top:3378px;width:330px;font-size:10.5px;line-height:14px;color:#666}
.field{position:absolute;font-size:10.5px;color:#888;border-bottom:1px solid var(--line);padding-bottom:10px}
.select{display:flex;align-items:center;gap:10px;width:140px}

/* Footer */
.footer{left:0;top:3571px;width:1200px;height:325px;background:var(--darker);color:#bbb}
.footer h5{position:absolute;top:60px;font-size:11px;color:var(--white);font-weight:700;letter-spacing:.5px}
.footer-brand{position:absolute;left:130px;top:160px;font-size:12px;letter-spacing:3px;color:#ddd;text-transform:uppercase}
.footer-about{position:absolute;left:130px;top:190px;width:290px;font-size:8.5px;line-height:12px;color:#888}
.footer-services{position:absolute;left:525px;top:98px;list-style:none;font-size:9.5px;line-height:20px;color:#bbb;text-transform:uppercase}
.footer-services li::before{content:"";display:inline-block;width:5px;height:5px;background:var(--white);margin-right:8px;vertical-align:middle}
.news{position:absolute;left:810px;width:260px;font-size:8.5px;line-height:12px;color:#888}
.news span{display:block;text-align:right;color:var(--white);margin-top:6px}
</style>
</head>
<body>

<section class="abs hero" aria-label="Hero">
  <div class="abs hero-skyline" role="img" aria-label="London city skyline silhouette"></div>
  <div class="abs hero-kicker">What differentiates us from other advisers ?</div>
  <h1 class="abs hero-title">Our genuine motivation to see our<br>clients succeed.</h1>
</section>

<div class="abs topbar">
  <div class="item" style="left:84px">
    <svg viewBox="0 0 14 14" fill="none" stroke="#ddd" stroke-width="1.2"><rect x="1" y="1" width="12" height="12"/><path d="M4 4c0 4 2 6 6 6l1-1.5-2-1-1 1c-1-.5-2-1.5-2.5-2.5l1-1-1-2z" fill="#ddd" stroke="none"/></svg>
    1.800.555.0147
  </div>
  <div class="item" style="left:255px">
    <svg viewBox="0 0 14 14" fill="none" stroke="#ddd" stroke-width="1.2"><rect x="1" y="1" width="12" height="12"/><path d="M7 3a3 3 0 0 1 3 3c0 2-3 5-3 5S4 8 4 6a3 3 0 0 1 3-3z" fill="#ddd" stroke="none"/></svg>
    LONDON, UK &nbsp; 714.0198
  </div>
  <div class="item" style="left:1090px">LOGIN</div>
</div>

<header class="abs masthead">
  <div class="brand">Quorvel Group</div>
  <nav class="nav">
    <a class="active">HOME</a><a>CLIENTS</a><a>PARTNERS</a><a>SERVICES</a><a>CONTACT</a>
  </nav>
</header>

<!-- Who we are -->
<h2 class="abs h2 display who-title">Who We Are</h2>
<p class="abs who-quote">I believe that through knowledge and discipline, financial peace is possible for all of us</p>
<div class="abs who-body">
  <p>Since founding Quorvel Group in 2014 we have dedicated ourselves to the provision of services. What differentiates us from other advisers or consultancies is a genuine motivation to see our clients succeed. Today's technology allows our clients to take their knowledge to the market in ways that previous generations could only dream of.</p>
  <p>That's why QG is dedicated to seeing you choose the right technology strategy, ensuring you maintain a competitive edge over your peers.</p>
</div>
<div class="abs who-sign">Quorvel Group</div>
<div class="abs who-panel">
  <p>Today's technology allows our clients to take their knowledge to the market in ways that previous generations could only dream of.</p>
</div>

<!-- What we do -->
<h2 class="abs h2 display what-title">What We Do</h2>
<p class="abs what-intro">QG is dedicated to seeing you choose the right technology strategy, ensuring you maintain a competitive edge over your peers.</p>

<article class="service" style="left:244px">
  <div class="photo" role="img" aria-label="Financial charts and documents on a desk" style="background:linear-gradient(135deg,#f3e4e6,#e9b8be 60%,#d98a93)"></div>
  <h3><span class="dot"></span>Financial Service</h3>
  <p>A trust is a way of managing assets (money, investments, land or buildings) for people – types of trust, how they are taxed, where to get help.</p>
</article>
<article class="service" style="left:491px">
  <div class="photo" role="img" aria-label="Stock market trading screen" style="background:linear-gradient(135deg,#1d2f55,#7a3a4a 55%,#d9743a)"></div>
  <h3><span class="dot"></span>Tax &amp; Finances</h3>
  <p>A trust is a way of managing assets (money, investments, land or buildings) for people – types of trust, how they are taxed, where to get help.</p>
</article>
<article class="service" style="left:738px">
  <div class="photo" role="img" aria-label="Business research with laptop in warm light" style="background:linear-gradient(135deg,#c7514a,#e9a06a 55%,#f6e3c0)"></div>
  <h3><span class="dot"></span>Research &amp; Training</h3>
  <p>A trust is a way of managing assets (money, investments, land or buildings) for people – types of trust, how they are taxed, where to get help.</p>
</article>

<!-- CTA -->
<section class="abs cta">
  <h2 class="display">Do you feel you need professional advice</h2>
  <p>That is simple to understand and straightforward to implement.</p>
  <div class="cta-btn">CALL TO ACTION</div>
</section>

<!-- Why choose us -->
<div class="abs why-photo" role="img" aria-label="Smiling adviser in a light blue shirt holding a tablet"></div>
<h2 class="abs h2 display why-title">Why Choose Us?</h2>
<p class="abs why-body">A trust is a way of managing assets (money, investments, land or buildings) for people – types of trust, how they are taxed, where to get help. A trust is a way of managing assets (money, investments, land or buildings) for people – types of trust, how they are taxed, where to get help.</p>

<div class="feature" style="left:597px;top:2160px"><h4><span class="dot"></span>Board Level Advisory</h4><p>A trust is a way of managing assets (money, investments, land or buildings) for people – types of trust, how they are taxed, where to get help.</p></div>
<div class="feature" style="left:836px;top:2160px"><h4><span class="dot"></span>Board Level Advisory</h4><p>A trust is a way of managing assets (money, investments, land or buildings) for people – types of trust, how they are taxed, where to get help.</p></div>
<div class="feature" style="left:597px;top:2285px"><h4><span class="dot"></span>Board Level Advisory</h4><p>A trust is a way of managing assets (money, investments, land or buildings) for people – types of trust, how they are taxed, where to get help.</p></div>
<div class="feature" style="left:836px;top:2285px"><h4><span class="dot"></span>Board Level Advisory</h4><p>A trust is a way of managing assets (money, investments, land or buildings) for people – types of trust, how they are taxed, where to get help.</p></div>

<!-- Team -->
<section class="abs team" role="img" aria-label="Meeting room with red overlay">
  <h2 class="abs h2 display team-title">Meet Our Team</h2>
  <p class="abs team-lead">It's all about the people</p>
  <p class="abs team-body">From planning and strategy, to technology and marketing, the individuals that make up XYZ Company share a passion for financial success, which influences everything we do. We prefer insourcing to outsourcing, so you have a team that understands your needs and is passionate about your success. The result is consistently great work, and phenomenal results — that you're proud of and that we're proud of.</p>

  <div class="member" style="left:83px">
    <div class="frame"><div class="portrait" role="img" aria-label="Team member portrait"></div></div>
    <ul><li>MEET DANIEL HARTLEY</li><li>+44(0)20 7946 0321</li><li>+44(0)7700 900 482</li></ul>
  </div>
  <div class="member" style="left:457px">
    <div class="frame"><div class="portrait" role="img" aria-label="Team member portrait"></div></div>
    <ul><li>MEET DANIEL HARTLEY</li><li>+44(0)20 7946 0321</li><li>+44(0)7700 900 482</li></ul>
  </div>
  <div class="member" style="left:831px">
    <div class="frame"><div class="portrait" role="img" aria-label="Team member portrait"></div></div>
    <ul><li>MEET DANIEL HARTLEY</li><li>+44(0)20 7946 0321</li><li>+44(0)7700 900 482</li></ul>
  </div>
</section>

<!-- Contact -->
<h2 class="abs display contact-title">Reach Out to Us</h2>
<p class="abs contact-body">Lorem ipsum dolor sit amet, consectetur adipiscing elit. Integer interdum sem ac magna. Integer in lectus sed ligula commodo commodo. In molestie neque at porta lobortis. Ligula sem auctor mauris, a luctus arcu quam sit amet augue. Aliquam eu felis. Nullam vel erat. Phasellus sed nibh nonummy, elit amet.</p>
<div class="field select" style="left:571px;top:3330px">Nothing selected
  <svg width="8" height="6" viewBox="0 0 8 6"><path d="M0 0h8L4 6z" fill="#888"/></svg>
</div>
<div class="field" style="left:571px;top:3395px;width:215px">First name</div>
<div class="field" style="left:820px;top:3395px;width:232px">Last name</div>
<div class="field" style="left:571px;top:3460px;width:215px">Email</div>
<div class="field" style="left:820px;top:3460px;width:232px">Phone number</div>

<!-- Footer -->
<footer class="abs footer">
  <h5 style="left:130px">ABOUT US</h5>
  <div class="footer-brand">Quorvel Group</div>
  <p class="footer-about">Since founding Quorvel Group in 2014 we have dedicated ourselves to the provision of services. What differentiates us from other advisers is a genuine motivation to see our clients succeed, today and tomorrow, with clear strategy.</p>

  <h5 style="left:525px">SERVICES</h5>
  <ul class="footer-services">
    <li>Investment Management</li><li>Financial Planning</li><li>Tax &amp; Trusts</li><li>Insurance Solutions</li>
    <li>Property Management</li><li>Investment Management</li><li>Financial Planning</li><li>Tax &amp; Trusts</li>
  </ul>

  <h5 style="left:810px">RECENT NEWS</h5>
  <div class="news" style="top:98px">New case study on trading infrastructure for a regional exchange now available.<span>Read more ▸</span></div>
  <div class="news" style="top:160px">Our latest brochure explains how we support buy side and sell side firms.<span>Read more ▸</span></div>
  <div class="news" style="top:222px">We welcome two new partners to strengthen our advisory work in Asia.<span>Read more ▸</span></div>
</footer>

</body>
</html>
```